Create a premium soap bar box bar design for an all-natural, men's skincare brand.

We are launching a men’s premium, natural soap bar and skincare business. To start, we will be launching cold-press, all-natural soap bars with a few additional products such as lotions. We plan to expand our line into additional skincare products such as face exfoliants, moisturizers and cleansers that target basic needs such as anti-aging, clarifying and hydrating.

Our target audience is men ages 25-50, with a secondary audience of male teens. Our target audience are mid to high income, professionals that live in more urban areas, but enjoy being active outdoors after work and on the weekends. Our target audience are hard workers, humble and want to enjoy all that life has to offer – whether that’s on top of a mountain or an ocean wave. They hike, bike, skateboard, surf or any other sport that gets them outside. They are husbands, brothers and fathers – there for their family and friends.

Our brand is sophisticated, adventurous and has a sense of humor. Many of our competitors either focus on the rugged outdoors or are more pretentious. We are in-between. We are free spirited and love the fresh air. Our products are trustworthy with no toxic chemicals or harsh ingredients. We are all-natural and provide high-quality, premium products that our audience expects and deserves.

Target Market(s)

Men, ages 25-54 who are high-earning professionals, yet enjoy getting outdoors and being active on the weekends - hiking, biking, surfing, skateboarding and more.

Industry/Entity Type

Men's skincare

Font styles to use
Sans Serif

Requirements
Must have
• See attachments
Nice to have
• We would prefer to a have a premium, slightly more modern looking design that will appeal to our target audience and slightly higher price point.
Should not have
• Please do not include an icon for the fragrance, i.e. cinnamon sticks. However, we do need some differentiation for the fragrance, i.e. color, etc. as it will be on the shelf with other fragrances.

```html
<!DOCTYPE html>
<html lang="en">
<head>
<meta charset="utf-8">
<title>Northwood Co. – Men's Natural Soap Box</title>
<link rel="stylesheet" href="https://fonts.googleapis.com/css2?family=Jost:wght@500;700;800&display=swap">
<style>
  :root {
    --kraft: #b99b70;
    --navy: #203448;
    --coral: #e8544a;
    --white: #ffffff;
  }
  html, body {
    margin: 0;
    padding: 0;
    width: 1200px;
    height: 1200px;
    overflow: hidden;
    background: var(--kraft);
  }
  .box-top {
    position: relative;
    width: 1200px;
    height: 1200px;
    background: var(--kraft);
    font-family: "Jost", sans-serif;
    color: var(--navy);
  }
  .frame-line, .landscape {
    position: absolute;
    inset: 0;
  }
  .brand-name {
    position: absolute;
    right: 60px;
    top: 160px;
    margin: 0;
    font-weight: 500;
    font-size: 60px;
    letter-spacing: 3px;
    line-height: 1;
    color: var(--navy);
  }
  .product-title {
    position: absolute;
    left: 215px;
    top: 300px;
    margin: 0;
    font-weight: 800;
    font-size: 150px;
    line-height: 0.9;
    letter-spacing: -3px;
    text-transform: uppercase;
    color: var(--navy);
  }
  .net-weight {
    position: absolute;
    left: 760px;
    top: 1040px;
    margin: 0;
    font-weight: 700;
    font-size: 58px;
    color: var(--white);
  }
</style>
</head>
<body>
<main class="box-top">
  <svg class="frame-line" width="1200" height="1200" viewBox="0 0 1200 1200" aria-hidden="true">
    <path d="M575 125 H112 V800" fill="none" stroke="var(--navy)" stroke-width="14"/>
  </svg>

  <p class="brand-name">NORTHWOOD CO.</p>

  <h1 class="product-title">Men’s<br>Natural<br>Soap</h1>

  <svg class="landscape" width="1200" height="1200" viewBox="0 0 1200 1200">
    <rect x="640" y="690" width="260" height="150" fill="var(--coral)" opacity="0.85" role="img" aria-label="Two stylised pine trees on a hillside"/>
    <path d="M0 790 C250 760 520 830 720 930 C900 1010 1050 880 1200 700 V1200 H0 Z" fill="var(--navy)"/>
    <path d="M560 845 C720 860 850 890 950 820 C1040 760 1120 700 1200 660 V720 C1090 860 990 960 860 960 C760 960 660 880 560 845 Z" fill="var(--coral)"/>
  </svg>

  <p class="net-weight">5 Oz. Bar</p>
</main>
</body>
</html>
```